Photographer's price list

I am a photographer who runs a studio (Pinefield Studio) and need to have a document to send clients detailing my packages (collections) and prices. I have written the text in a word document and need a designer to lay it out for me using my logo and two specific fonts: DejaVu Sans and LainieDaySH.

The look should be clean and modern and keep in the same style as my logo. I will primarily be using the final product as a PDF file to email to potential clients. It should stay black and white.

I would also like to be able to update the text myself as my prices and packages change. So I would like a PSD file.

I think I would like for the document to be in landscape format with "Collections" on one side and A la Carte on the other, but I am open to other ideas.

As for sizing, it should be a standard size so that clients can print it out if they like.

Requirements
Must have
• my logo
fonts: DejaVu and LainieDaySH
Easy to email
Easy to display on one page upon opening
Standard size so that printing from a home computer is easy to do.

```html
<!DOCTYPE html>
<html lang="en">
<head>
<meta charset="utf-8">
<title>2013 Photography Collections – Pinefield Studio</title>
<link rel="stylesheet" href="https://fonts.googleapis.com/css2?family=Allura&family=Open+Sans:wght@400&display=swap">
<style>
  :root {
    --ink: #111111;
    --muted: #9a9a9a;
    --ornament: #ececec;
    --paper: #ffffff;
  }
  * { margin: 0; padding: 0; box-sizing: border-box; }
  html, body { width: 1200px; height: 848px; overflow: hidden; background: var(--paper); }
  .sheet {
    position: relative;
    width: 1200px; height: 848px;
    background: var(--paper);
    color: var(--ink);
    font-family: "Open Sans", Verdana, sans-serif;
    font-size: 13px;
    line-height: 17.5px;
    overflow: hidden;
  }
  .ornament { position: absolute; }
  .ornament--top-left { left: 0; top: 0; width: 300px; height: 150px;
    background: radial-gradient(ellipse at 20% 30%, var(--ornament), transparent 70%); }
  .ornament--top-right { right: 0; top: 0; width: 230px; height: 180px;
    background: radial-gradient(ellipse at 80% 30%, var(--ornament), transparent 70%); }
  .ornament--left-edge { left: 0; top: 280px; width: 90px; height: 480px;
    background: radial-gradient(ellipse at 10% 50%, var(--ornament), transparent 70%); }
  .ornament--right-edge { right: 0; top: 230px; width: 80px; height: 520px;
    background: radial-gradient(ellipse at 90% 50%, var(--ornament), transparent 70%); }
  .ornament--bottom-band { left: 0; bottom: 0; width: 1200px; height: 40px;
    background: linear-gradient(to top, var(--ornament), transparent); }

  .title {
    position: absolute; left: 0; top: 34px; width: 1200px;
    text-align: center;
    font-family: "Allura", cursive;
    font-size: 54px; line-height: 60px; font-weight: 400;
  }
  .column { position: absolute; text-align: center; }
  .column--collections { left: 15px; width: 500px; }
  .column--a-la-carte { left: 710px; width: 490px; }
  .block { position: absolute; left: 0; width: 100%; }
  .script-heading {
    font-family: "Allura", cursive; font-weight: 400;
    font-size: 38px; line-height: 40px;
  }
  .script-heading--small { font-size: 29px; line-height: 30px; }
  .script-heading .amount { font-size: 34px; }
  .count { color: var(--muted); }
  .price {
    font-family: "Allura", cursive; color: var(--muted);
    font-size: 19px; margin-left: 6px;
  }
  .dividers { position: absolute; left: 0; top: 0; }
  .studio-name {
    position: absolute; left: 480px; top: 404px; width: 260px;
    text-align: center;
    font-family: "Open Sans", Verdana, sans-serif;
    font-size: 22px; letter-spacing: 2px; line-height: 28px;
    color: var(--ink);
  }
</style>
</head>
<body>
<main class="sheet">
  <div class="ornament ornament--top-left" role="img" aria-label="Soft grey floral swirl ornament"></div>
  <div class="ornament ornament--top-right" role="img" aria-label="Soft grey floral swirl ornament"></div>
  <div class="ornament ornament--left-edge" role="img" aria-label="Soft grey floral swirl ornament"></div>
  <div class="ornament ornament--right-edge" role="img" aria-label="Soft grey floral swirl ornament"></div>
  <div class="ornament ornament--bottom-band" role="img" aria-label="Soft grey floral border ornament"></div>

  <svg class="dividers" width="1200" height="848" aria-hidden="true">
    <g fill="none" stroke="var(--ink)" stroke-width="2">
      <circle cx="590" cy="200" r="40"/>
      <circle cx="590" cy="637" r="40"/>
      <circle cx="600" cy="776" r="26"/>
    </g>
  </svg>
  <div class="studio-name">Pinefield Studio</div>

  <h1 class="title">2013 photography collections</h1>

  <section class="column column--collections">
    <h2 class="block script-heading" style="top:134px">all collections include:</h2>
    <p class="block" style="top:180px">
      One to two hour portrait session with photographer in location<br>
      of your choice (unlimited time if necessary!)<br>
      Clara will create a presentation video with hand-selected music<br>
      and custom editing, which tells your story, highlights the best images,<br>
      and reveals the connections within your family.<br>
      An online gallery for viewing and ordering helps you share your images<br>
      with family and friends.
    </p>

    <h2 class="block script-heading" style="top:334px">Collection 1: <span class="amount">300 €</span></h2>
    <p class="block" style="top:375px">
      Your favorite <span class="count">five</span> images from the session will be professionally<br>
      edited and presented to you on disk as<br>
      high resolution jpegs
    </p>

    <h2 class="block script-heading" style="top:447px">Collection 2: <span class="amount">400 €</span></h2>
    <p class="block" style="top:488px">
      Your favorite <span class="count">ten</span> images from the session will be professionally edited<br>
      and given to you on disk as high resolution jpegs<br>
      Your favorite image from the session will be professionally printed<br>
      for you (20x30cm) on Vellmark paper, Clara’s favorite for portraits.
    </p>

    <h2 class="block script-heading" style="top:580px">Collection 3: <span class="amount">500 €</span></h2>
    <p class="block" style="top:618px">
      Your favorite <span class="count">fifteen</span> images from the session will be professionally edited<br>
      and presented to you on disk as high resolution jpegs<br>
      Your favorite <span class="count">two</span> images from the session will be professionally printed<br>
      for you (20x30cm) on Vellmark paper, Clara’s favorite for portraits.
    </p>

    <h2 class="block script-heading" style="top:703px">Collection 4: <span class="amount">600 €</span></h2>
    <p class="block" style="top:742px">
      <span class="count">ALL</span> presented images from the session will be professionally edited<br>
      and presented to you on disk as high resolution jpegs (approx. 40+ images)<br>
      Your favorite <span class="count">two</span> images from the session will be professionally printed<br>
      for you (20x30cm) on Vellmark paper, Clara’s favorite for portraits.
    </p>
  </section>

  <section class="column column--a-la-carte">
    <h2 class="block script-heading" style="top:106px">a la carte pricing</h2>
    <p class="block" style="top:150px">
      These products may be purchased separately to complement your<br>
      collection. A consultation with Clara will help you decide which products<br>
      are best for gifts and for your home.
    </p>

    <h3 class="block script-heading script-heading--small" style="top:224px">high resolution digital images</h3>
    <p class="block" style="top:262px">
      Perfect if you just need to add “one more image” to your collection!<br>
      High-resolution jpeg file <span class="price">25 €</span> each
    </p>

    <h3 class="block script-heading script-heading--small" style="top:308px">matt prints</h3>
    <p class="block" style="top:340px">
      20x30 cm and smaller <span class="price">25 €</span><br>
      Each print is professionally edited, printed on archival photo paper.<br>
      Purchase includes the JPEG file for your personal digital use.
    </p>

    <h3 class="block script-heading script-heading--small" style="top:405px">vellmark prints</h3>
    <p class="block" style="top:442px">
      Prints on Vellmark (watercolor) paper are Clara’s favorite for<br>
      large format color prints<br>
      30x40 cm <span class="price">45 €</span>
    </p>

    <h3 class="block script-heading script-heading--small" style="top:501px">canvas prints</h3>
    <p class="block" style="top:534px">
      Ready-to-hang, stretched canvas wall art of your favorite images<br>
      30x40 cm <span class="price">100 €</span>
    </p>

    <h3 class="block script-heading script-heading--small" style="top:582px">framed + matted prints</h3>
    <p class="block" style="top:613px">
      Beautiful Vellmark prints finished with wide mats and simple,<br>
      elegant frames of your choice<br>
      30x40 inch <span class="price">350 €</span>
    </p>

    <h3 class="block script-heading script-heading--small" style="top:675px">custom designed albums</h3>
    <p class="block" style="top:710px">
      Images from your session are selected for the custom design of an album<br>
      and bound in a book for a modern presentation of your images.<br>
      There are a number of cover choices for the classic flush-mount and<br>
      beautifully crafted albums. A great way to display all of your favorite<br>
      images from your session on your coffee table.<br>
      Prices begin at <span class="price">100 €</span>
    </p>
  </section>
</main>
</body>
</html>
```